Creative Landscape Architecture Company Needs a Creative Business Card Design

Marsh and Partners, Inc. is a landscape architecture (LA) company started in 1997 in Austin, TX. We work on large commerical projects all around the U.S. and provide land planning, site planning, landscape design and architectural renderings.

We don't want this card to look like a LA firm's business card. We are looking for a business card design that is edgy and cool to reflect the more artistic and creative side of our company. We would like our clients to think "now there's a business card unlike any other LA that I've seen before."

We would like it to be in standard 2"x3.5" format. Double sided. Full color ok. Our company logo is attached. We like the logo but would not be adverse to any variations you would like to make to it. Feel free to change it up. Typically the logo has been a light saturated orange color but its not necessary that you stick with it.

Requirements
Must have
• 1. Company name
2. individuals name
3. email address
4. cell number
5. office number
6. website: www.marshandpartners-demo.net
7. Business address
Nice to have
• Can add (but not necessary)
Personal titles such as "president" or "registered landscape architect"

```html
<!DOCTYPE html>
<html lang="en">
<head>
<meta charset="utf-8">
<title>Marsh and Partners, Inc. – Business Card</title>
<link href="https://fonts.googleapis.com/css2?family=Courgette&display=swap" rel="stylesheet">
<style>
  :root {
    --paper: #fffbc2;
    --edge: #3a3a3a;
    --ink: #111111;
    --leaf-dark: #0b0b0b;
    --leaf-yellow: #f3e21c;
    --leaf-pale: #f6ef9c;
    --ring: #ffe60a;
    --ring-line: #b8a600;
    --ring-hole: #ffffff;
    --stage: #ffffff;
  }
  * { box-sizing: border-box; margin: 0; padding: 0; }
  html, body { width: 1200px; height: 378px; overflow: hidden; background: var(--stage); }
  .canvas { position: relative; width: 1200px; height: 378px; }

  .card {
    position: absolute;
    background: var(--paper);
    border: 1px solid var(--edge);
    overflow: hidden;
  }
  .card--portrait { width: 173px; height: 241px; }
  .card--landscape { width: 241px; height: 173px; z-index: 2; }

  .ring {
    position: absolute;
    width: 22px; height: 22px;
    border-radius: 50%;
    background: var(--ring);
    border: 1px solid var(--ring-line);
    z-index: 3;
  }
  .ring::after {
    content: "";
    position: absolute;
    left: 5px; top: 5px;
    width: 10px; height: 10px;
    border-radius: 50%;
    background: var(--ring-hole);
    border: 1px solid var(--ring-line);
  }

  .artwork { position: absolute; border-radius: 4px; }
  .artwork--bold {
    background:
      radial-gradient(ellipse at 45% 55%, rgba(243,226,28,0.55) 0%, rgba(243,226,28,0.18) 35%, rgba(11,11,11,0) 60%),
      var(--leaf-dark);
  }
  .artwork--faint {
    background:
      radial-gradient(ellipse at 45% 55%, rgba(243,226,28,0.45) 0%, rgba(243,226,28,0) 60%),
      var(--leaf-pale);
    opacity: 0.85;
  }

  .details { position: absolute; inset: 0; font-family: "Courgette", cursive; color: var(--ink); }
  .details > * { position: absolute; white-space: nowrap; }
  .company { top: 30px; left: 0; right: 0; text-align: center; font-size: 14px; font-weight: 700; text-decoration: underline; }
  .person { top: 70px; right: 12px; font-size: 10px; }
  .rule { left: 14px; right: 12px; height: 1px; background: var(--ink); }
  .rule--name { top: 83px; }
  .title { top: 84px; left: 14px; font-size: 9.5px; }
  .office { top: 110px; left: 14px; font-size: 7px; }
  .address { top: 119px; right: 17px; text-align: right; font-size: 7.5px; line-height: 10px; }
  .phone { top: 155px; right: 12px; font-size: 8.5px; }
  .cell { top: 167px; right: 12px; font-size: 8.5px; }
  .rule--contact { top: 180px; }
  .web { top: 183px; left: 0; right: 0; text-align: center; font-size: 6.5px; }
  .email { top: 193px; left: 0; right: 0; text-align: center; font-size: 6.5px; }
</style>
</head>
<body>
<main class="canvas">

  <section class="card card--portrait" style="left:78px; top:67px;">
    <div class="artwork artwork--bold" style="left:24px; top:27px; width:124px; height:192px;" role="img" aria-label="Black leaf silhouette with yellow branching veins"></div>
  </section>
  <span class="ring" style="left:79px; top:67px;"></span>

  <section class="card card--portrait" style="left:273px; top:67px;">
    <div class="artwork artwork--faint" style="left:26px; top:27px; width:120px; height:190px;" role="img" aria-label="Faint leaf outline with yellow branching veins"></div>
  </section>
  <span class="ring" style="left:274px; top:67px;"></span>

  <section class="card card--portrait" style="left:468px; top:67px;">
    <div class="artwork artwork--faint" style="left:22px; top:40px; width:130px; height:190px;" role="img" aria-label="Pale leaf illustration with yellow veins behind the text"></div>
    <div class="details">
      <p class="company">Marsh and Partners,</p>
      <p class="person">Mr. C. D. Hale</p>
      <span class="rule rule--name"></span>
      <p class="title">Registered landscape architect</p>
      <p class="office">Marsh &amp; Partners - Austin - Central</p>
      <p class="address">210 Meridian Ln<br>Suite 140<br>Riverton, TX 78701</p>
      <p class="phone">Office: (512) 555-0142</p>
      <p class="cell">Cell: (512) 555-0187</p>
      <span class="rule rule--contact"></span>
      <p class="web">http://www.marshandpartners-demo.net</p>
      <p class="email">cdhale@marshandpartners-demo.net</p>
    </div>
  </section>
  <span class="ring" style="left:469px; top:67px;"></span>

  <section class="card card--portrait" style="left:897px; top:64px;">
    <div class="artwork artwork--faint" style="left:22px; top:40px; width:130px; height:190px;" role="img" aria-label="Pale leaf illustration with yellow veins behind the text"></div>
    <div class="details">
      <p class="company">Marsh and Partners,</p>
      <p class="person">Mr. C. D. Hale</p>
      <span class="rule rule--name"></span>
      <p class="title">Registered landscape architect</p>
      <p class="office">Marsh &amp; Partners - Austin - Central</p>
      <p class="address">210 Meridian Ln<br>Suite 140<br>Riverton, TX 78701</p>
      <p class="phone">Office: (512) 555-0142</p>
      <p class="cell">Cell: (512) 555-0187</p>
      <span class="rule rule--contact"></span>
      <p class="web">http://www.marshandpartners-demo.net</p>
      <p class="email">cdhale@marshandpartners-demo.net</p>
    </div>
  </section>

  <section class="card card--landscape" style="left:681px; top:64px;">
    <div class="artwork artwork--bold" style="left:27px; top:24px; width:188px; height:128px;" role="img" aria-label="Black leaf silhouette with yellow branching veins, turned sideways"></div>
  </section>
  <span class="ring" style="left:898px; top:63px;"></span>

</main>
</body>
</html>
```